BRIGHTVALE ADVISERS POWERPOINT PRESENTATION TEMPLATE 1

We need the ultimate quality Powerpoint presentation design.
We are the advisory firm working with modern world class tech companies throughout Europe, their founders, shareholders, and potential investors.
The new template must contain elements such as our logo, appropriate backgrounds, be at the same time very attractive visually and easy to rear. Also there must be some place where logo of our clients should be placed.

We like:
- icons and
- infographics,
so attractive design in this area will be greatly appreciated.

Please avoid serif fonts and excessive decorations such as "waves" or other similar decor.

We are also in contact with serious investors - wealthy individuals, reputable financial institutions, and their advisers; banks, private equity investors, global technology companies.

The Powerpoint template design must send a message that:
- we are a high technology oriented team of professionals,
- we provide modern financial advisory services
- but at the same time we are open minded, creative, yet very competent in the area of corporate finance.

The Powerpoint template must complement our business card design, first impression of a team of top notch professionals who advise top notch tech companies on their top notch corporate finance and M&A projects.

Enclosed are sets of our logo, current template, business card project which won previous competition.

It is perhaps a good basis to start with and get us to the template of our dreams.

While working on this project please think about the following firms which at some point may be looking at your design:
- Quorlin
- Tavindex
- Pelorim
- Veskaran (Zundle)
- Marowisp
- Turnequo
- Dovrash
- Kelvaro
- Obrethy

The quality of the design, its style, aesthetics must meet the top criteria in contemporary design trends.

Target Market(s)

Banks, financial investors, strategic investors

Industry/Entity Type

Finance

Font styles to use
Sans Serif

Requirements
Must have
• Icons
Infographics
Attractive backgrounds
Clean design
Harmonize with logo and emblem colors.
Should not have
• Excessive tacky decor (waves, etc)
Serif fonts
Excessive colors

```html
<!DOCTYPE html>
<html lang="en">
<head>
<meta charset="utf-8">
<title>Brightvale Advisers – Presentation Template</title>
<link href="https://fonts.googleapis.com/css2?family=Poppins:ital,wght@0,300;0,400;0,500;0,600;0,800;1,300;1,400&display=swap" rel="stylesheet">
<style>
:root{
  --page:#dfe9f5;
  --navy:#1d3c78;
  --deep:#173a6f;
  --blue:#2b78c2;
  --sky:#1fa6e0;
  --purple:#6b4aa8;
  --indigo:#3a2d7a;
  --ink:#3b4356;
  --muted:#6a7283;
  --card:#f6f7f9;
  --white:#ffffff;
}
*{margin:0;padding:0;box-sizing:border-box}
html,body{width:1200px;height:2700px;overflow:hidden}
body{background:var(--page);font-family:'Poppins',Arial,sans-serif;color:var(--ink);position:relative}
.slide{position:absolute;width:518px;height:291px;background:var(--card);overflow:hidden;box-shadow:0 14px 22px rgba(40,70,120,.22)}
.col-l{left:62px}.col-r{left:620px}
.abs{position:absolute}
.gradient{background:linear-gradient(20deg,#1a3f82 0%,#2476b9 55%,#34a7df 100%)}
.s-title{position:absolute;left:28px;top:20px;font-weight:800;font-size:18px;color:var(--navy);letter-spacing:-.2px;line-height:1.2}
.s-sub{position:absolute;left:28px;top:46px;font-size:8.5px;color:var(--sky);text-transform:uppercase}
.brand{position:absolute;right:24px;top:22px;display:flex;align-items:center;gap:4px;font-size:11px;font-weight:400;color:var(--navy)}
.brand .dot{width:12px;height:12px;border-radius:50%;background:var(--navy)}
.body-xs{font-size:7px;line-height:1.35;color:var(--ink)}
.body-xxs{font-size:5.6px;line-height:1.35;color:var(--ink)}
.footer-band{position:absolute;left:0;bottom:0;width:100%;height:18px;background:linear-gradient(90deg,#1d3c78,#2a8ad0 60%,#34a7df);color:#fff;font-size:6px;padding:6px 32px}
/* cover */
.cover .word{position:absolute;left:286px;top:68px;color:#fff;font-weight:300;font-size:17px;letter-spacing:.3px}
.cover .title{position:absolute;left:286px;top:103px;color:#fff;font-weight:800;font-size:19px;line-height:1.25}
.cover .rule{position:absolute;left:286px;top:165px;width:28px;height:2px;background:#fff}
.cover .lead{position:absolute;left:286px;top:175px;width:200px;color:#fff;font-style:italic;font-weight:300;font-size:8px;line-height:1.3}
.cover .copy{position:absolute;left:286px;top:238px;color:#fff;font-size:6px}
/* agenda */
.agenda-item{position:absolute;display:flex;gap:10px;width:210px}
.num{flex:none;width:30px;height:30px;border-radius:50%;color:#fff;font-weight:600;font-size:12px;display:flex;align-items:center;justify-content:center}
.agenda-item h4{font-size:7.5px;font-weight:600;color:var(--navy);margin-bottom:3px}
/* swot */
.swot-label{position:absolute;font-size:8px;font-weight:600;color:var(--navy)}
.swot-text{position:absolute;width:130px;font-size:7.5px;line-height:1.3}
/* strategy */
.step{position:absolute;width:92px}
.step .yr{font-weight:600;font-size:12px;color:var(--navy)}
.step .bar{height:6px;margin:6px 0 8px}
.step .nm{font-size:8px;font-weight:600;color:var(--blue);margin-bottom:3px}
/* timeline */
.tl-text{position:absolute;width:60px;font-size:7px;line-height:1.2}
/* testimonial */
.t-card{position:absolute;width:138px;height:106px;background:#fff;border-radius:6px;box-shadow:0 4px 10px rgba(20,50,100,.15);padding:10px}
.t-card .avatar{position:absolute;left:10px;top:10px;width:40px;height:40px;border-radius:50%;background:linear-gradient(#8a9099,#c5c9cf)}
.t-card .nm{position:absolute;left:66px;top:18px;font-size:8px;font-weight:600;color:var(--navy)}
.t-card .st{position:absolute;left:66px;top:30px;font-size:5.5px;font-style:italic;color:var(--muted)}
.t-card p{position:absolute;left:10px;top:58px;width:120px;font-size:6.5px;line-height:1.25}
/* two column */
.col-text{position:absolute;top:105px;width:224px;text-align:justify}
/* key points */
.kp{position:absolute;left:250px;display:flex;gap:12px;width:245px}
.kp .ic{flex:none;width:34px;height:34px;border-radius:50%;display:flex;align-items:center;justify-content:center}
.kp h4{font-size:8px;font-weight:600;color:var(--navy);margin-bottom:2px}
.kp p{font-size:6.5px;line-height:1.3}
</style>
</head>
<body>

<!-- Row 1: covers -->
<section class="slide col-l cover gradient" style="top:145px">
  <div class="word">BRIGHTVALE</div>
  <div class="title">YOUR PRESENTATION<br>GOES HERE</div>
  <div class="rule"></div>
  <p class="lead">Lorem Ipsum is simply dummy text of the printing and typesetting industry. Lorem Ipsum has been the industry's standard dummy text ever since the 1500s</p>
  <div class="copy">© 2020 Brightvale</div>
</section>
<section class="slide col-r cover gradient" style="top:145px">
  <div class="word">BRIGHTVALE</div>
  <div class="title">YOUR PRESENTATION<br>GOES HERE</div>
  <div class="rule"></div>
  <p class="lead">Lorem Ipsum is simply dummy text of the printing and typesetting industry. Lorem Ipsum has been the industry's standard dummy text ever since the 1500s</p>
  <div class="copy">© 2020 Brightvale</div>
</section>

<!-- Row 2: agenda + title with image -->
<section class="slide col-l" style="top:497px">
  <h2 class="s-title">AGENDA SLIDE GOES HERE</h2>
  <div class="s-sub">Your subtitle goes here</div>
  <div class="brand"><span class="dot"></span>BRIGHTVALE</div>
  <div class="agenda-item" style="left:42px;top:100px"><div class="num" style="background:var(--blue)">01</div><div><h4>Heading here</h4><p class="body-xs">Lorem ipsum is simply dummy text of the printing and typesetting industry.</p></div></div>
  <div class="agenda-item" style="left:42px;top:165px"><div class="num" style="background:var(--sky)">02</div><div><h4>Heading here</h4><p class="body-xs">Lorem ipsum is simply dummy text of the printing and typesetting industry.</p></div></div>
  <div class="agenda-item" style="left:42px;top:230px"><div class="num" style="background:var(--navy)">03</div><div><h4>Heading here</h4><p class="body-xs">Lorem ipsum is simply dummy text of the printing and typesetting industry.</p></div></div>
  <div class="agenda-item" style="left:282px;top:100px"><div class="num" style="background:var(--blue)">04</div><div><h4>Heading here</h4><p class="body-xs">Lorem ipsum is simply dummy text of the printing and typesetting industry.</p></div></div>
  <div class="agenda-item" style="left:282px;top:165px"><div class="num" style="background:var(--sky)">05</div><div><h4>Heading here</h4><p class="body-xs">Lorem ipsum is simply dummy text of the printing and typesetting industry.</p></div></div>
  <div class="agenda-item" style="left:282px;top:230px"><div class="num" style="background:var(--navy)">06</div><div><h4>Heading here</h4><p class="body-xs">Lorem ipsum is simply dummy text of the printing and typesetting industry.</p></div></div>
</section>
<section class="slide col-r" style="top:497px;background:#fff">
  <div class="brand" style="left:32px;right:auto;top:80px;font-size:16px"><span class="dot" style="width:18px;height:18px"></span>BRIGHTVALE</div>
  <div class="abs" style="left:34px;top:122px;font-weight:800;font-size:19px;line-height:1.3;color:var(--blue)">YOUR PRESENTATION<br>GOES HERE</div>
  <p class="abs" style="left:34px;top:190px;width:230px;font-size:8px;font-style:italic;line-height:1.3">Lorem Ipsum is simply dummy text of the printing and typesetting industry. Lorem Ipsum has been the industry's standard dummy text ever since the 1500s</p>
  <div class="abs" role="img" aria-label="Photograph of modern glass office towers" style="left:318px;top:42px;width:180px;height:180px;border-radius:50%;background:linear-gradient(160deg,#9fb6cf,#2e5d8e 60%,#1b3458)"></div>
  <div class="footer-band">© 2020 Brightvale</div>
</section>

<!-- Row 3: SWOT + mountain -->
<section class="slide col-l" style="top:849px">
  <h2 class="s-title">SWOT SLIDE GOES HERE</h2>
  <div class="s-sub">Your subtitle goes here</div>
  <div class="brand"><span class="dot"></span>BRIGHTVALE</div>
  <svg class="abs" style="left:0;top:0" width="518" height="291" viewBox="0 0 518 291">
    <g font-family="Poppins, sans-serif" font-weight="600" font-size="20" fill="#fff">
      <path d="M183 172 A75 75 0 0 1 256 97 L256 141 A31 31 0 0 0 227 172 Z" fill="#1fa6e0"/>
      <path d="M260 97 A75 75 0 0 1 333 172 L289 172 A31 31 0 0 0 260 141 Z" fill="#2b6fc0"/>
      <path d="M183 176 A75 75 0 0 0 256 249 L256 205 A31 31 0 0 1 227 176 Z" fill="#1d3c78"/>
      <path d="M260 249 A75 75 0 0 0 333 176 L289 176 A31 31 0 0 1 260 205 Z" fill="#2b5da8"/>
      <text x="210" x2="0" y="160">S</text><text x="282" y="163">W</text>
      <text x="213" y="210">O</text><text x="288" y="210">T</text>
    </g>
    <circle cx="191" cy="126" r="13" fill="#1fa6e0" stroke="#fff" stroke-width="2"/>
    <path d="M184 126h14M185 123v6M197 123v6" stroke="#fff" stroke-width="1.6"/>
    <circle cx="328" cy="126" r="13" fill="#2b6fc0" stroke="#fff" stroke-width="2"/>
    <circle cx="328" cy="126" r="5" fill="none" stroke="#fff" stroke-width="1.5"/>
    <circle cx="191" cy="218" r="13" fill="#1d3c78" stroke="#fff" stroke-width="2"/>
    <rect x="185" y="214" width="12" height="9" rx="1.5" fill="#fff"/>
    <circle cx="328" cy="218" r="13" fill="#2b5da8" stroke="#fff" stroke-width="2"/>
    <circle cx="328" cy="220" r="5" fill="#fff"/>
  </svg>
  <div class="swot-label" style="right:358px;top:97px">STRENGHT</div>
  <p class="swot-text" style="left:30px;top:110px;text-align:right">Lorem Ipsum is simply dummy text of the printing. Lorem Ipsum has been the industry's standard dummy text</p>
  <div class="swot-label" style="left:358px;top:97px">WEAKNESS</div>
  <p class="swot-text" style="left:358px;top:110px">Lorem Ipsum is simply dummy text of the printing. Lorem Ipsum has been the industry's standard dummy text</p>
  <div class="swot-label" style="right:358px;top:210px">OPPORTUNITY</div>
  <p class="swot-text" style="left:30px;top:223px;text-align:right">Lorem Ipsum is simply dummy text of the printing. Lorem Ipsum has been the industry's standard dummy text</p>
  <div class="swot-label" style="left:358px;top:210px">THREAT</div>
  <p class="swot-text" style="left:358px;top:223px">Lorem Ipsum is simply dummy text of the printing. Lorem Ipsum has been the industry's standard dummy text</p>
</section>
<section class="slide col-r" style="top:849px">
  <h2 class="s-title">MOUNTAIN DIAGRAM GOES HERE</h2>
  <div class="s-sub">Your subtitle goes here</div>
  <div class="brand"><span class="dot"></span>BRIGHTVALE</div>
  <svg class="abs" style="left:0;top:0" width="518" height="291" viewBox="0 0 518 291">
    <g opacity=".92">
      <path d="M30 243 Q80 238 100 178 Q120 238 170 243Z" fill="#2b78c2"/>
      <path d="M95 243 Q145 238 165 150 Q185 238 235 243Z" fill="#1d4f9a"/>
      <path d="M160 243 Q210 238 228 175 Q246 238 296 243Z" fill="#2b8ad0"/>
      <path d="M220 243 Q272 238 290 138 Q308 238 360 243Z" fill="#1d4f9a"/>
      <path d="M285 243 Q337 238 355 122 Q373 238 425 243Z" fill="#2b78c2"/>
      <path d="M345 243 Q397 238 415 185 Q433 238 485 243Z" fill="#2b5da8"/>
    </g>
    <g fill="#2b78c2" stroke="#fff" stroke-width="2">
      <circle cx="100" cy="156" r="13"/><circle cx="165" cy="128" r="13"/><circle cx="228" cy="153" r="13"/>
      <circle cx="290" cy="116" r="13"/><circle cx="355" cy="100" r="13"/><circle cx="415" cy="163" r="13"/>
    </g>
    <g fill="none" stroke="#fff" stroke-width="1.4">
      <circle cx="99" cy="155" r="4"/><path d="M102 158l4 4"/>
      <path d="M159 131h12a3 3 0 0 0-2-6a4 4 0 0 0-8 1a3 3 0 0 0-2 5z"/>
      <circle cx="228" cy="151" r="4"/><path d="M226 157h4"/>
      <circle cx="290" cy="116" r="5"/><circle cx="290" cy="116" r="2"/>
      <path d="M349 98h4l6-4v12l-6-4h-4z"/>
      <rect x="409" y="158" width="12" height="9" rx="1"/>
    </g>
    <g font-family="Poppins, sans-serif" font-size="9" fill="#3b4356" text-anchor="middle">
      <text x="100" y="262">January</text><text x="165" y="262">February</text><text x="228" y="262">March</text>
      <text x="290" y="262">April</text><text x="355" y="262">May</text><text x="415" y="262">June</text>
    </g>
  </svg>
</section>

<!-- Row 4: strategy + timeline -->
<section class="slide col-l" style="top:1201px">
  <div class="abs" style="left:22px;top:22px;font-weight:800;font-size:18px;line-height:1.2;color:var(--navy)">STRATEGY SLIDE<br>GOES HERE</div>
  <div class="abs" style="left:22px;top:70px;font-size:8.5px;color:var(--sky)">YOUR SUBTITLE GOES HERE</div>
  <svg class="abs" style="left:0;top:0" width="518" height="291" viewBox="0 0 518 291">
    <defs><linearGradient id="wedge" x1="0" x2="1"><stop offset="0" stop-color="#2b8ad0"/><stop offset="1" stop-color="#1d3c78"/></linearGradient></defs>
    <path d="M215 291 L518 200 L518 291Z" fill="url(#wedge)"/>
  </svg>
  <div class="brand" style="top:260px;color:#fff"><span class="dot" style="background:#fff"></span>BRIGHTVALE</div>
  <div class="step" style="left:45px;top:172px"><div class="yr">2018</div><div class="bar" style="background:var(--sky)"></div><div class="nm">Lorem Ipsum</div><p class="body-xxs">Lorem ipsum is simply dummy text of the printing and typesetting industry.<br><br>Lorem ipsum has been the industry's standard dummy text ever since the 1500s</p></div>
  <div class="step" style="left:161px;top:132px"><div class="yr">2019</div><div class="bar" style="background:var(--blue)"></div><div class="nm">Lorem Ipsum</div><p class="body-xxs">Lorem ipsum is simply dummy text of the printing and typesetting industry.<br><br>Lorem ipsum has been the industry's standard dummy text ever since the 1500s</p></div>
  <div class="step" style="left:277px;top:92px"><div class="yr">2020</div><div class="bar" style="background:#2b5da8"></div><div class="nm">Lorem Ipsum</div><p class="body-xxs">Lorem ipsum is simply dummy text of the printing and typesetting industry.<br><br>Lorem ipsum has been the industry's standard dummy text ever since the 1500s</p></div>
  <div class="step" style="left:393px;top:52px"><div class="yr">2021</div><div class="bar" style="background:var(--navy)"></div><div class="nm">Lorem Ipsum</div><p class="body-xxs">Lorem ipsum is simply dummy text of the printing and typesetting industry.<br><br>Lorem ipsum has been the industry's standard dummy text ever since the 1500s</p></div>
</section>
<section class="slide col-r" style="top:1201px">
  <h2 class="s-title">TIMELINE SLIDE GOES HERE</h2>
  <div class="s-sub">Your subtitle goes here</div>
  <div class="brand"><span class="dot"></span>BRIGHTVALE</div>
  <svg class="abs" style="left:0;top:0" width="518" height="291" viewBox="0 0 518 291">
    <line x1="20" y1="169" x2="480" y2="169" stroke="#1d3c78" stroke-width="2"/>
    <circle cx="20" cy="169" r="3.5" fill="#1d3c78"/><circle cx="480" cy="169" r="3.5" fill="#1d3c78"/>
    <g stroke="#3b4356" stroke-width=".8">
      <line x1="65" y1="82" x2="65" y2="158"/><line x1="213" y1="82" x2="213" y2="158"/><line x1="361" y1="82" x2="361" y2="158"/>
      <line x1="139" y1="180" x2="139" y2="256"/><line x1="287" y1="180" x2="287" y2="256"/><line x1="435" y1="180" x2="435" y2="256"/>
    </g>
    <g fill="#3b4356"><circle cx="139" cy="256" r="1.6"/><circle cx="287" cy="256" r="1.6"/><circle cx="435" cy="256" r="1.6"/><circle cx="65" cy="82" r="1.6"/><circle cx="213" cy="82" r="1.6"/><circle cx="361" cy="82" r="1.6"/></g>
    <g stroke="#1d3c78" stroke-width="2">
      <circle cx="65" cy="169" r="11" fill="#1d3c78"/><circle cx="139" cy="169" r="11" fill="#1fa6e0"/>
      <circle cx="213" cy="169" r="11" fill="#2b5da8"/><circle cx="287" cy="169" r="11" fill="#1fa6e0"/>
      <circle cx="361" cy="169" r="11" fill="#2b78c2"/><circle cx="435" cy="169" r="11" fill="#1fa6e0"/>
    </g>
    <g font-family="Poppins, sans-serif" font-size="8" font-weight="600" fill="#fff" text-anchor="middle">
      <text x="65" y="172">1</text><text x="139" y="172">2</text><text x="213" y="172">3</text><text x="287" y="172">4</text><text x="361" y="172">5</text><text x="435" y="172">6</text>
    </g>
  </svg>
  <p class="tl-text" style="left:74px;top:80px">Lorem Ipsum is simply dummy text of the printing and typesetting industry.</p>
  <p class="tl-text" style="left:222px;top:80px">Lorem Ipsum is simply dummy text of the printing and typesetting industry.</p>
  <p class="tl-text" style="left:370px;top:80px">Lorem Ipsum is simply dummy text of the printing and typesetting industry.</p>
  <p class="tl-text" style="left:148px;top:202px">Lorem Ipsum is simply dummy text of the printing and typesetting industry.</p>
  <p class="tl-text" style="left:296px;top:202px">Lorem Ipsum is simply dummy text of the printing and typesetting industry.</p>
  <p class="tl-text" style="left:444px;top:202px">Lorem Ipsum is simply dummy text of the printing and typesetting industry.</p>
</section>

<!-- Row 5: break + testimonial -->
<section class="slide col-l" style="top:1553px;background:#fff">
  <div class="abs" style="left:40px;top:80px;font-weight:800;font-size:19px;line-height:1.3;color:var(--blue)">YOUR BREAK SLIDE<br>GOES HERE</div>
  <div class="abs" style="left:40px;top:144px;width:46px;height:2px;background:var(--navy)"></div>
  <p class="abs" style="left:40px;top:165px;width:200px;font-size:8px;font-style:italic;line-height:1.3">Lorem Ipsum is simply dummy text of the printing and typesetting industry. Lorem Ipsum has been the industry's standard dummy text ever since the 1500s</p>
  <div class="footer-band">© 2020 Brightvale</div>
</section>
<section class="slide col-r" style="top:1553px;background:#fff">
  <div class="abs" style="left:0;top:0;width:95px;height:291px;background:linear-gradient(#2fa2dc,#1d4f9a)"></div>
  <div class="t-card" style="left:26px;top:36px"><div class="avatar" role="img" aria-label="Portrait photo of client"></div><div class="nm">Name here</div><div class="st">Subtitle here</div><p>Lorem Ipsum is simply dummy text of the printing. Lorem Ipsum has been the industry's standard dummy text</p></div>
  <div class="t-card" style="left:178px;top:36px"><div class="avatar" role="img" aria-label="Portrait photo of client"></div><div class="nm">Name here</div><div class="st">Subtitle here</div><p>Lorem Ipsum is simply dummy text of the printing. Lorem Ipsum has been the industry's standard dummy text</p></div>
  <div class="t-card" style="left:26px;top:158px"><div class="avatar" role="img" aria-label="Portrait photo of client"></div><div class="nm">Name here</div><div class="st">Subtitle here</div><p>Lorem Ipsum is simply dummy text of the printing. Lorem Ipsum has been the industry's standard dummy text</p></div>
  <div class="t-card" style="left:178px;top:158px"><div class="avatar" role="img" aria-label="Portrait photo of client"></div><div class="nm">Name here</div><div class="st">Subtitle here</div><p>Lorem Ipsum is simply dummy text of the printing. Lorem Ipsum has been the industry's standard dummy text</p></div>
  <div class="brand"><span class="dot"></span>BRIGHTVALE</div>
  <div class="abs" style="left:362px;top:60px;font-weight:800;font-size:44px;line-height:1;color:#e3e6ea">“</div>
  <div class="abs" style="left:362px;top:100px;font-weight:800;font-size:17px;line-height:1.3;color:var(--navy)">TESTIMONIAL<br>SLIDE HERE</div>
  <div class="abs" style="left:362px;top:152px;font-size:8px;color:var(--sky)">YOUR SUBTITLE GOES HERE</div>
  <p class="abs body-xxs" style="left:362px;top:188px;width:130px;text-align:justify">Lorem Ipsum is simply dummy text of the printing and typesetting industry. Lorem Ipsum has been the industry's standard dummy text ever since the 1500s, when an unknown printer took a galley of type and scrambled it to make a type specimen book.</p>
</section>

<!-- Row 6: chart + two column -->
<section class="slide col-l" style="top:1905px">
  <h2 class="s-title">TIMELINE SLIDE GOES HERE</h2>
  <div class="s-sub">Your subtitle goes here</div>
  <div class="brand"><span class="dot"></span>BRIGHTVALE</div>
  <svg class="abs" style="left:0;top:0" width="518" height="291" viewBox="0 0 518 291">
    <g font-family="Poppins, sans-serif" font-size="7" fill="#3b4356" text-anchor="end">
      <text x="42" y="101">70</text><text x="42" y="123">60</text><text x="42" y="145">50</text><text x="42" y="167">40</text>
      <text x="42" y="189">30</text><text x="42" y="211">20</text><text x="42" y="233">10</text><text x="42" y="255">0</text>
    </g>
    <line x1="52" y1="253" x2="305" y2="253" stroke="#c5cad3" stroke-width="1"/>
    <g>
      <rect x="66" y="158" width="10" height="95" fill="#1fa6e0"/><rect x="77" y="200" width="10" height="53" fill="#6b4aa8"/><rect x="88" y="209" width="10" height="44" fill="#3a2d7a"/>
      <rect x="129" y="198" width="10" height="55" fill="#1fa6e0"/><rect x="140" y="154" width="10" height="99" fill="#6b4aa8"/><rect x="151" y="187" width="10" height="66" fill="#3a2d7a"/>
      <rect x="192" y="207" width="10" height="46" fill="#1fa6e0"/><rect x="203" y="213" width="10" height="40" fill="#6b4aa8"/><rect x="214" y="165" width="10" height="88" fill="#3a2d7a"/>
      <rect x="255" y="147" width="10" height="106" fill="#1fa6e0"/><rect x="266" y="191" width="10" height="62" fill="#6b4aa8"/><rect x="277" y="125" width="10" height="128" fill="#3a2d7a"/>
    </g>
    <g font-family="Poppins, sans-serif" font-size="7" fill="#3b4356" text-anchor="middle">
      <text x="82" y="266">2015</text><text x="145" y="266">2016</text><text x="208" y="266">2017</text><text x="271" y="266">2018</text>
    </g>
  </svg>
  <div class="abs" style="left:342px;top:125px;width:140px">
    <h4 style="font-size:8px;font-weight:600;color:var(--navy);margin-bottom:4px">Heading here</h4>
    <p class="body-xs">Lorem Ipsum is simply dummy text of the printing and typesetting industry. Lorem Ipsum has been the industry's standard dummy text</p>
    <h4 style="font-size:8px;font-weight:600;color:var(--navy);margin:14px 0 4px">Heading here</h4>
    <p class="body-xs">Lorem Ipsum is simply dummy text of the printing and typesetting industry. Lorem Ipsum has been the industry's standard dummy text</p>
  </div>
</section>
<section class="slide col-r" style="top:1905px">
  <h2 class="s-title">TWO COLUMN TEXT GOES HERE</h2>
  <div class="s-sub">Your subtitle goes here</div>
  <div class="brand"><span class="dot"></span>BRIGHTVALE</div>
  <div class="col-text body-xxs" style="left:28px"><p>Contrary to popular belief, Lorem Ipsum is not simply random text. It has roots in a piece of classical Latin literature from 45 BC, making it over 2000 years old. A professor at a college in Virginia looked up one of the more obscure Latin words, consectetur, from a Lorem Ipsum passage, and going through the cites of the word in classical literature, discovered the undoubtable source. Lorem Ipsum comes from sections 1.10.32 and 1.10.33 of "de Finibus Bonorum et Malorum" (The Extremes of Good and Evil), written in 45 BC. This book is a treatise on the theory of ethics, very popular during the Renaissance.</p><p style="margin-top:6px">The standard chunk of Lorem Ipsum used since the 1500s is reproduced below for those interested. Sections 1.10.32 and 1.10.33 are also reproduced in their exact original form, accompanied by English versions from the 1914 translation.</p></div>
  <div class="col-text body-xxs" style="left:268px"><p>It is a long established fact that a reader will be distracted by the readable content of a page when looking at its layout. The point of using Lorem Ipsum is that it has a more-or-less normal distribution of letters, as opposed to using 'Content here, content here', making it look like readable English. Many desktop publishing packages and web page editors now use Lorem Ipsum as their default model text, and a search will uncover many web sites still in their infancy.</p><p style="margin-top:6px">There are many variations of passages of Lorem Ipsum available, but the majority have suffered alteration in some form, by injected humour, or randomised words which don't look even slightly believable. All the Lorem Ipsum generators on the Internet tend to repeat predefined chunks as necessary, making this the first true generator on the Internet.</p></div>
</section>

<!-- Row 7: key points + closing -->
<section class="slide col-l" style="top:2257px">
  <div class="brand" style="left:22px;right:auto;top:90px"><span class="dot"></span>BRIGHTVALE</div>
  <div class="abs" style="left:22px;top:125px;font-weight:800;font-size:17px;line-height:1.3;color:var(--navy)">FOUR KEY POINTS<br>GOES HERE</div>
  <div class="abs" style="left:22px;top:178px;font-size:8px;color:var(--sky)">YOUR SUBTITLE GOES HERE</div>
  <div class="kp" style="top:40px"><div class="ic" style="background:var(--sky)"><svg width="16" height="16" viewBox="0 0 16 16" fill="none" stroke="#fff" stroke-width="1.5"><circle cx="7" cy="7" r="4.5"/><path d="M10.5 10.5L14 14"/></svg></div><div><h4>Lorem ipsum</h4><p>Lorem Ipsum is simply dummy text of the printing and typesetting industry. Lorem Ipsum has been the industry's standard dummy text ever since the 1500s</p></div></div>
  <div class="kp" style="top:98px"><div class="ic" style="background:var(--blue)"><svg width="16" height="16" viewBox="0 0 16 16" fill="none" stroke="#fff" stroke-width="1.5"><path d="M3 11h10a3 3 0 0 0-1-6a5 5 0 0 0-9 1a3 3 0 0 0 0 5z"/></svg></div><div><h4>Lorem ipsum</h4><p>Lorem Ipsum is simply dummy text of the printing and typesetting industry. Lorem Ipsum has been the industry's standard dummy text ever since the 1500s</p></div></div>
  <div class="kp" style="top:156px"><div class="ic" style="background:#2b5da8"><svg width="16" height="16" viewBox="0 0 16 16" fill="none" stroke="#fff" stroke-width="1.5"><circle cx="8" cy="6.5" r="4"/><path d="M6 13h4"/></svg></div><div><h4>Lorem ipsum</h4><p>Lorem Ipsum is simply dummy text of the printing and typesetting industry. Lorem Ipsum has been the industry's standard dummy text ever since the 1500s</p></div></div>
  <div class="kp" style="top:214px"><div class="ic" style="background:var(--navy)"><svg width="16" height="16" viewBox="0 0 16 16" fill="none" stroke="#fff" stroke-width="1.5"><circle cx="8" cy="8" r="6"/><circle cx="8" cy="8" r="2.5"/></svg></div><div><h4>Lorem ipsum</h4><p>Lorem Ipsum is simply dummy text of the printing and typesetting industry. Lorem Ipsum has been the industry's standard dummy text ever since the 1500s</p></div></div>
</section>
<section class="slide col-r" style="top:2257px">
  <div class="abs" role="img" aria-label="Blue-toned photograph of office skyscrapers" style="left:0;top:0;width:518px;height:291px;background:linear-gradient(200deg,#2d6fb4 0%,#245a9e 50%,#1b4582 100%)"></div>
  <div class="abs" style="left:36px;top:100px;color:#fff;font-weight:300;font-size:17px">BRIGHTVALE</div>
  <div class="abs" style="left:36px;top:140px;color:#fff;font-weight:800;font-size:19px;line-height:1.3">THANK YOU FOR<br>WATCHING</div>
</section>

</body>
</html>
```